New Business Card Design Project

We need to enhance the look and feel of our brand. We are starting with the business card and will hopefully expand to letter head, website, etc. The firm is based in Kolding Denmark and invests with global pension funds and for mutual fund investors alike. We would like to see an innovative use of the companies logo (star on the website - www.tidemarkharbor.com) and a broader use of a color palette. Presently it is dominantly shades of blue. The firm wants to convey a sense they are a creative investment team that understands all the risks in the emerging markets and have the skills to perform in an environment of uncertainty.

Presently, we have three locations: Kolding Denmark, Glendale CA USA, Zurich Switzerland. We also have a prominently displayed bar code square on a solid dark blue back that will take smart phone users to the firm's website. I am indifferent to its inclusion., Details for my new Business Card Design Project will be added soon.
Updates

Reason: Designers, I am working with on getting feedback from both US and Danish partners on preferences. That is taking slightly more time than expected. Thanks for you patience. Nice work. PLM

Target Market(s)

The target market is a combination of institutional and retail investors. The european arm uses a card similar to a couple of those submitted.

Industry/Entity Type

Environment

Requirements
Must have
• The company's Star Logo. See www.tidemarkharbor.com. It may be used in its current form or some new clever way. The founders are Danish and have a strong affinity for it.
Nice to have
• The new materials may be solely used in the north America and distributed in Australia as well. Therefore, we may try something new in these markets. I'd prefer to see a broader use of the color spectrum, not simply blue.
Should not have
• The card should not look and feel like a bank, insurance company, or a traditional money manager.

```html
<!DOCTYPE html>
<html lang="en">
<head>
<meta charset="utf-8">
<title>Tidemark Harbor – Business Card</title>
<link href="https://fonts.googleapis.com/css2?family=Arimo:wght@400;700&display=swap" rel="stylesheet">
<style>
  :root {
    --backdrop: #ece8e2;
    --card-dark: #3a3a3a;
    --space-deep: #1536b8;
    --space-mid: #2f7fe0;
    --space-light: #6fd2f2;
    --text-light: #ffffff;
    --text-soft: #d8d8d8;
    --brand-blue: #2a9fe0;
  }
  html, body {
    margin: 0;
    width: 1200px;
    height: 1200px;
    overflow: hidden;
    background: var(--backdrop);
    font-family: "Arimo", Arial, sans-serif;
  }
  .sheet {
    width: 1200px;
    height: 1200px;
    display: flex;
    flex-direction: column;
    align-items: center;
    justify-content: center;
    gap: 70px;
  }
  .card {
    position: relative;
    width: 700px;
    height: 390px;
    border-radius: 30px;
    background: var(--card-dark);
    overflow: hidden;
    box-shadow: 0 6px 18px rgba(0,0,0,0.25);
  }
  .space-panel {
    position: absolute;
    top: 0;
    bottom: 0;
    left: 0;
    background: linear-gradient(160deg, var(--space-deep) 0%, var(--space-mid) 45%, var(--space-light) 100%);
  }
  .card-front .space-panel { width: 190px; }
  .card-back .space-panel { width: 250px; }

  .brand {
    position: absolute;
    left: 190px;
    right: 0;
    top: 110px;
    display: flex;
    flex-direction: column;
    align-items: center;
    gap: 26px;
  }
  .brand-mark {
    width: 92px;
    height: 92px;
    border-radius: 50%;
    background: var(--brand-blue);
  }
  .brand-name {
    font-size: 42px;
    font-weight: 700;
    color: var(--brand-blue);
    letter-spacing: 0.5px;
  }

  .person {
    position: absolute;
    left: 300px;
    top: 60px;
  }
  .person-name {
    font-size: 32px;
    color: var(--text-light);
    margin: 0;
  }
  .person-role {
    font-size: 20px;
    color: var(--text-soft);
    margin: 14px 0 0;
  }
  .contact {
    position: absolute;
    left: 300px;
    bottom: 60px;
    font-size: 15px;
    line-height: 1.25;
    color: var(--text-light);
  }
  .contact p { margin: 0; }
  .contact .web { font-weight: 700; }
  .globe-decor {
    position: absolute;
    right: -30px;
    bottom: -40px;
    width: 160px;
    height: 160px;
    border-radius: 50%;
    background: radial-gradient(circle, rgba(255,255,255,0.35), rgba(255,255,255,0.08));
  }
</style>
</head>
<body>
<main class="sheet">
  <section class="card card-front">
    <div class="space-panel" role="img" aria-label="Blue starry space background with a white wireframe globe"></div>
    <div class="brand">
      <div class="brand-mark"></div>
      <div class="brand-name">Tidemark Harbor</div>
    </div>
  </section>

  <section class="card card-back">
    <div class="space-panel" role="img" aria-label="Blue starry space background"></div>
    <div class="person">
      <p class="person-name">Name</p>
      <p class="person-role">Ocupación</p>
    </div>
    <div class="contact">
      <p>2140 Harbor Lane  Tampa, FL 33602, Estados Unidos</p>
      <p>+1 813-555-0142</p>
      <p>tell.: 45550187 - Fax.: 66550294</p>
      <p>personname@tidemarkharbor.com</p>
      <p class="web">www.tidemarkharbor.com</p>
    </div>
    <div class="globe-decor" role="img" aria-label="White wireframe globe illustration"></div>
  </section>
</main>
</body>
</html>
```